Business Card Design

Please use the Logo for colors and styles, and create a business card using the following info:

Matthias Loeber
Web Developer

Loeber Solutions
+41 76 482 17 05
matthias@loeber-solutions.example
www.loeber-solutions.example

Download the logo at http://loeber-solutions.example/tl_files/loeber_solutions.zip

Thanks for your works!

```html
<!DOCTYPE html>
<html lang="en">
<head>
<meta charset="utf-8">
<title>Loeber Solutions – Business Card</title>
<link rel="stylesheet" href="https://fonts.googleapis.com/css2?family=Arimo:wght@400;500;700&family=EB+Garamond:wght@400&display=swap">
<style>
  :root {
    --brand-blue: #1a7fc4;
    --brand-navy: #0f4a77;
    --card-top: #0079c6;
    --card-bottom: #0f4a76;
    --paper: #ffffff;
    --stage-dark: #0f4a77;
    --stage-light: #1a8bd2;
    --floor-top: #0a7cc4;
    --floor-bottom: #0c4776;
    --label: #0f3a5e;
  }
  * { margin: 0; padding: 0; box-sizing: border-box; }
  html, body { width: 1200px; height: 900px; overflow: hidden; background: var(--paper); }
  .board { position: relative; width: 1200px; height: 900px; font-family: "Arimo", Arial, sans-serif; }

  .brand-header {
    position: absolute; top: 0; left: 0; width: 1200px; height: 210px;
    display: flex; align-items: center; justify-content: center; background: var(--paper);
  }
  .wordmark {
    font-family: "Arimo", Arial, sans-serif; font-weight: 500;
    text-transform: uppercase; letter-spacing: 1px; line-height: 1; white-space: nowrap;
  }
  .brand-header .wordmark { font-size: 74px; color: var(--brand-blue); }

  .stage {
    position: absolute; top: 210px; left: 0; width: 1200px; height: 445px;
    background: linear-gradient(to bottom, var(--stage-dark) 0%, var(--stage-dark) 35%, var(--stage-light) 88%, #cfe8f8 99%, #ffffff 100%);
  }
  .floor {
    position: absolute; top: 655px; left: 0; width: 1200px; height: 245px;
    background: linear-gradient(to bottom, var(--floor-top), var(--floor-bottom));
  }

  .card {
    position: absolute; top: 281px; width: 510px; height: 290px;
    box-shadow: 6px 8px 12px rgba(0, 20, 45, 0.55);
  }
  .card-front { left: 62px; background: var(--paper); color: var(--brand-navy); }
  .card-back {
    left: 635px;
    background: linear-gradient(to bottom, var(--card-top) 0, var(--card-top) 144px, var(--card-bottom) 144px);
    display: flex; align-items: center; justify-content: center;
  }

  .card-front .wordmark {
    position: absolute; top: 35px; left: 0; width: 100%; text-align: center;
    font-size: 41px; color: var(--brand-blue);
  }
  .card-back .wordmark { font-size: 41px; color: var(--paper); margin-top: 0; }

  .holder { position: absolute; top: 110px; left: 0; width: 100%; text-align: center; }
  .holder-name { font-size: 20px; font-weight: 500; letter-spacing: 1px; color: var(--brand-navy); }
  .holder-role { margin-top: 2px; font-size: 13px; letter-spacing: 1.6px; color: var(--brand-navy); text-transform: uppercase; }

  .divider { position: absolute; top: 172px; left: 8px; width: 494px; height: 8px; }

  .contact { position: absolute; top: 217px; left: 19px; list-style: none; font-size: 11.5px; letter-spacing: 0.8px; line-height: 15px; color: var(--brand-navy); }

  .side-label {
    position: absolute; top: 603px; font-family: "EB Garamond", Georgia, serif;
    font-size: 16px; letter-spacing: 2.5px; color: var(--label); text-transform: uppercase;
  }
  .side-label.front { left: 86px; }
  .side-label.back { left: 658px; }
</style>
</head>
<body>
  <main class="board">
    <header class="brand-header">
      <div class="wordmark">Loeber Solutions</div>
    </header>

    <section class="stage"></section>
    <section class="floor"></section>

    <article class="card card-front" aria-label="Card front">
      <div class="wordmark">Loeber Solutions</div>
      <div class="holder">
        <p class="holder-name">Matthias Loeber</p>
        <p class="holder-role">Web Developer</p>
      </div>
      <svg class="divider" viewBox="0 0 494 8" preserveAspectRatio="none" aria-hidden="true">
        <path d="M0 5 Q120 2.5 247 3 T494 5 L494 5.6 Q370 6.4 247 6 T0 5.4 Z" fill="var(--brand-blue)"/>
      </svg>
      <ul class="contact">
        <li>Loeber Solutions</li>
        <li>Phone: +41 76 482 17 05</li>
        <li>Web: www.loeber-solutions.example</li>
        <li>Email: matthias@loeber-solutions.example</li>
      </ul>
    </article>

    <article class="card card-back" aria-label="Card back">
      <div class="wordmark">Loeber Solutions</div>
    </article>

    <p class="side-label front">Front</p>
    <p class="side-label back">Back</p>
  </main>
</body>
</html>
```